Food truck menu design

Looking for a menu to be dissed for my toasted sandwich food truck. I have attached to logo and photo of the food truck for inspiration. if it can tie into them.
needing three sections, with titles:
CLASSICS
- classic one
. description
-Classic two
. Description
PREMIUM
- Premium one
. description
-Premium Two
. Description
-Premium Three
. Description
DESERT
-Desert one
. Description
-Desert two
.Description

also if it can be editable so I can change menu items and descriptions.

```html
<!DOCTYPE html>
<html lang="en">
<head>
<meta charset="UTF-8">
<title>Milo's Melts – Menu</title>
<link rel="stylesheet" href="https://fonts.googleapis.com/css2?family=Delius&family=Kaushan+Script&family=Questrial&family=Mulish:wght@700&display=swap">
<style>
  :root {
    --bg: #0d0d0d;
    --pattern: #111111;
    --orange: #f7a11a;
    --cream: #fff6e6;
    --desc: #d8cdc2;
    --frame: #7d7d7d;
    --box: #ecdfd2;
  }
  * { margin: 0; padding: 0; box-sizing: border-box; }
  html, body { width: 1200px; height: 927px; overflow: hidden; background: var(--bg); }
  .menu { position: relative; width: 1200px; height: 927px; background: var(--bg); overflow: hidden; }
  .menu-pattern { position: absolute; inset: 0; background: var(--pattern); }
  .menu-frame {
    position: absolute; left: 26px; top: 31px; width: 1145px; height: 865px;
    border: 2px solid var(--frame); border-radius: 44px;
  }
  .brand {
    position: absolute; left: 130px; top: 180px; width: 344px;
    display: flex; align-items: center; justify-content: center; gap: 14px;
  }
  .brand-dot { width: 34px; height: 34px; border-radius: 50%; background: var(--orange); flex: none; }
  .brand-name { font-family: "Delius", cursive; font-size: 44px; color: var(--cream); white-space: nowrap; }

  .section-title {
    position: absolute; font-family: "Kaushan Script", cursive; font-size: 62px;
    color: var(--orange); line-height: 1; text-align: center; transform: translateX(-50%);
  }
  .classics-title { left: 297px; top: 408px; }
  .premium-title { left: 884px; top: 70px; }

  .item { position: absolute; }
  .item-row {
    display: flex; align-items: baseline; white-space: nowrap;
    font-family: "Delius", cursive; color: var(--cream); font-size: 34px; line-height: 1;
  }
  .item-leader { flex: 1; overflow: hidden; letter-spacing: 1px; }
  .item-leader::before { content: "......................................................................"; }
  .item-price { font-family: "Mulish", sans-serif; font-weight: 700; font-size: 31px; margin-left: 4px; }
  .item-desc {
    font-family: "Questrial", sans-serif; color: var(--desc); font-size: 19px; line-height: 24px;
  }

  .classic { left: 120px; width: 390px; }
  .classic .item-desc { margin: 20px 0 0 23px; }
  .classic-1 { top: 505px; }
  .classic-2 { top: 661px; }

  .premium { left: 716px; width: 375px; }
  .premium .item-desc { margin: 12px 0 0 15px; }
  .premium-1 { top: 157px; }
  .premium-2 { top: 295px; }
  .premium-3 { top: 419px; }

  .dessert-box {
    position: absolute; left: 624px; top: 630px; width: 521px; height: 230px;
    border: 3px solid var(--box); border-radius: 29px;
  }
  .dessert-title {
    left: 887px; top: 596px; padding: 0 10px; background: var(--bg);
  }
  .dessert { left: 656px; width: 471px; }
  .dessert .item-row { font-size: 30px; }
  .dessert .item-price { font-size: 30px; }
  .dessert .item-desc { margin: 8px 0 0 30px; }
  .dessert-1 { top: 682px; }
  .dessert-2 { top: 763px; }
</style>
</head>
<body>
<main class="menu">
  <div class="menu-pattern" role="img" aria-label="Faint repeating pattern of toasted sandwich icons"></div>
  <div class="menu-frame"></div>

  <header class="brand">
    <span class="brand-dot"></span>
    <span class="brand-name">Milo's Melts</span>
  </header>

  <h2 class="section-title classics-title">Classics</h2>
  <article class="item classic classic-1">
    <div class="item-row"><span class="item-name">Classic one</span><span class="item-leader"></span><span class="item-price">$0.0</span></div>
    <p class="item-desc">description, description, description,<br>description, description, description.</p>
  </article>
  <article class="item classic classic-2">
    <div class="item-row"><span class="item-name">Classic one</span><span class="item-leader"></span><span class="item-price">$0.0</span></div>
    <p class="item-desc">description, description, description,<br>description, description, description.</p>
  </article>

  <h2 class="section-title premium-title">Premium</h2>
  <article class="item premium premium-1">
    <div class="item-row"><span class="item-name">Premium one</span><span class="item-leader"></span><span class="item-price">$0.0</span></div>
    <p class="item-desc">description, description, description,<br>description, description, description.</p>
  </article>
  <article class="item premium premium-2">
    <div class="item-row"><span class="item-name">Premium two</span><span class="item-leader"></span><span class="item-price">$0.0</span></div>
    <p class="item-desc">description, description, description,<br>description, description, description.</p>
  </article>
  <article class="item premium premium-3">
    <div class="item-row"><span class="item-name">Premium three</span><span class="item-leader"></span><span class="item-price">$0.0</span></div>
    <p class="item-desc">description, description, description,<br>description, description, description.</p>
  </article>

  <div class="dessert-box"></div>
  <h2 class="section-title dessert-title">Desert</h2>
  <article class="item dessert dessert-1">
    <div class="item-row"><span class="item-name">Desert one</span><span class="item-leader"></span><span class="item-price">$0.0</span></div>
    <p class="item-desc">description,description,description,</p>
  </article>
  <article class="item dessert dessert-2">
    <div class="item-row"><span class="item-name">Desert two</span><span class="item-leader"></span><span class="item-price">$0.0</span></div>
    <p class="item-desc">description,description,description</p>
  </article>
</main>
</body>
</html>
```